Business Card Design

We are starting up a new Family run Business mainly offering a Free House Clearance service. We also offer the following chargeable services which include a Removals Service, Delivery and Collection of Items sold or purchased on Bidloft, Swapcorner etc, including Motorcycles, Piano's, Furniture, Electrical appliances.
As there are a few Companies offering similar services we need to stand out and show what we do at a glance while appearing Professional and approachable
Updates

TidyNests

i  am liking some of the colours and designs so far but would like to see a few of our services listed as 1 or 2 have already done if this is possible and maybe some emphasis on the FREE House Clearance. thank you 
best regards
derek

Target Market(s)

Commercial and Domestic Tenants and Landlords aswell as Families looking for a friendly sympathetic clearance service after bereavement

Industry/Entity Type

Business

Contact Information for Business Card

TidyNests,
HouseClearance and Removals,
Brynmor Vale
CF47 2RL
Tel: 07831562904
Email: enquiries@tidynests.example

```html
<!DOCTYPE html>
<html lang="en">
<head>
<meta charset="utf-8">
<title>TidyNests business cards</title>
<link rel="stylesheet" href="https://fonts.googleapis.com/css2?family=Jost:wght@400;500&family=Cormorant+Garamond:wght@500&display=swap">
<style>
  :root {
    --green: #86bc3d;
    --green-dark: #6f9e2f;
    --green-soft: #a3cf67;
    --ink: #111111;
    --paper: #ffffff;
    --backdrop: #e9e9e9;
    --edge: #9a9a9a;
  }
  * { box-sizing: border-box; margin: 0; padding: 0; }
  html, body { width: 1200px; height: 1200px; overflow: hidden; }
  body {
    background: var(--backdrop);
    font-family: "Jost", sans-serif;
    position: relative;
  }
  .card {
    position: absolute;
    width: 525px;
    height: 300px;
    overflow: hidden;
    box-shadow: 0 6px 18px rgba(0,0,0,.18);
  }
  .card--front { left: 60px; top: 150px; background: var(--green); }
  .card--back { left: 615px; top: 150px; background: var(--paper); border: 1px solid var(--edge); }
  .card--contact { left: 337px; top: 620px; background: var(--green); }

  .wordmark { display: flex; align-items: center; gap: 12px; position: absolute; }
  .wordmark__dot { width: 40px; height: 40px; border-radius: 50%; flex: none; }
  .wordmark__name {
    font-weight: 500; font-size: 26px; letter-spacing: .5px; line-height: 1;
  }
  .wordmark__tag {
    font-weight: 500; font-size: 9.5px; letter-spacing: 1.2px; margin-top: 4px; line-height: 1;
  }

  .card--front .wordmark { left: 40px; top: 126px; }
  .card--front .wordmark__dot { background: var(--paper); }
  .card--front .wordmark__name, .card--front .wordmark__tag { color: var(--paper); }
  .front-feature {
    position: absolute; right: 0; top: 40px;
    width: 130px; height: 220px;
    background: var(--green-soft);
  }

  .card--back .wordmark { left: 125px; top: 126px; }
  .card--back .wordmark__dot { background: var(--green); }
  .card--back .wordmark__name { color: var(--green-dark); }
  .card--back .wordmark__tag { color: var(--ink); }

  .holder {
    position: absolute; right: 34px; top: 32px;
    font-size: 22px; letter-spacing: .5px; font-weight: 400;
  }
  .holder__first { color: var(--ink); }
  .holder__last { color: var(--paper); }

  .card--contact .wordmark { left: 34px; top: 112px; }
  .card--contact .wordmark__dot { background: var(--paper); width: 32px; height: 32px; }
  .card--contact .wordmark__name { color: var(--paper); font-size: 20px; }
  .card--contact .wordmark__tag { color: var(--paper); font-size: 8px; }

  .contact-list {
    position: absolute; left: 34px; top: 168px; list-style: none;
    font-family: "Cormorant Garamond", serif; color: var(--paper);
    font-size: 15px; letter-spacing: 1.6px; line-height: 1.25;
  }
  .contact-list li { display: flex; align-items: flex-start; gap: 12px; margin-bottom: 6px; }
  .contact-list svg { width: 16px; height: 16px; flex: none; margin-top: 2px; }
</style>
</head>
<body>

  <section class="card card--front" aria-label="Card front">
    <div class="wordmark">
      <span class="wordmark__dot"></span>
      <div>
        <div class="wordmark__name">TIDYNESTS</div>
        <div class="wordmark__tag">Free House Clearance service</div>
      </div>
    </div>
    <div class="front-feature" role="img" aria-label="Large cropped brand decoration"></div>
  </section>

  <section class="card card--back" aria-label="Card back">
    <div class="wordmark">
      <span class="wordmark__dot"></span>
      <div>
        <div class="wordmark__name">TIDYNESTS</div>
        <div class="wordmark__tag">Free House Clearance service</div>
      </div>
    </div>
  </section>

  <section class="card card--contact" aria-label="Contact side">
    <div class="holder"><span class="holder__first">DEREK</span> <span class="holder__last">HALE</span></div>
    <div class="wordmark">
      <span class="wordmark__dot"></span>
      <div>
        <div class="wordmark__name">TIDYNESTS</div>
        <div class="wordmark__tag">Free House Clearance service</div>
      </div>
    </div>
    <ul class="contact-list">
      <li>
        <svg viewBox="0 0 16 16" aria-hidden="true"><path d="M8 1a4.5 4.5 0 0 0-4.5 4.5C3.5 9 8 15 8 15s4.5-6 4.5-9.5A4.5 4.5 0 0 0 8 1zm0 6.2a1.7 1.7 0 1 1 0-3.4 1.7 1.7 0 0 1 0 3.4z" fill="#111"/></svg>
        <span>TidyNests, HouseClearance<br>and Removals, Brynmor Vale CF47 2RL</span>
      </li>
      <li>
        <svg viewBox="0 0 16 16" aria-hidden="true"><path d="M4 1.5 6.2 4 5 5.6c.8 1.9 2.3 3.4 4.2 4.2L10.8 8.6 13.5 10.8 12.3 13.6C7 13.4 2.6 9 2.4 3.7z" fill="#111"/></svg>
        <span>07831562904</span>
      </li>
      <li>
        <svg viewBox="0 0 16 16" aria-hidden="true"><rect x="1.5" y="3.5" width="13" height="9" rx="1" fill="#111"/><path d="M2 4.2 8 9l6-4.8" stroke="#86bc3d" stroke-width="1.2" fill="none"/></svg>
        <span>enquiries@tidynests.example</span>
      </li>
    </ul>
  </section>

</body>
</html>
```